Email Signature Design

Please design an email signature, the below is an example of our current design;
___

CARRODY ESTATE HOLDINGS PTY LTD
BENEDICT HARLOWE
Licensed Strata and Community Manager

143 Tallowood Street,
KELDARRA NSW 2093

P: 02.9473.6820 F: 9536.2048
Website: www.carrodyestate.com.au

This e-mail message and accompanying data may contain information that is confidential and private. If you are not the intended recipient, the use, dissemination, distribution or copying of this message or data is prohibited.

If you have received this e-mail in error please notify us immediately and delete all material pertaining to this e-mail. strata@carrodyestate.com.au

___

We would like to incorporate our logo and company colours, you can view the colours and feel of image at www.carrodyestate.com.au

Industry/Entity Type

It Company

Requirements
Must have
• use of logo and company colours (image)

```html
<!DOCTYPE html>
<html lang="en">
<head>
<meta charset="utf-8">
<title>Carrody Estate Holdings – Email Signature</title>
<link rel="stylesheet" href="https://fonts.googleapis.com/css2?family=Arimo:ital,wght@0,400;0,700;1,400&family=Cormorant+SC:wght@500&display=swap">
<style>
  :root {
    --ink: #1a1a1a;
    --grey-text: #555555;
    --gold: #9a7a1c;
    --rule: #8a8a8a;
    --link: #2a9fd6;
    --link-muted: #555555;
    --icon-blue: #3b6fb6;
    --icon-sky: #4fc3e8;
    --icon-navy: #1f6fb0;
    --eco-green: #2e8b3a;
    --band-top: #e4e4e2;
    --band-mid: #c9ccc6;
    --band-green: #7ccf3a;
    --foot-top: #cfcfcf;
    --foot-bottom: #f4f4f4;
  }
  * { margin: 0; padding: 0; box-sizing: border-box; }
  html, body { width: 1200px; height: 1022px; overflow: hidden; background: #ffffff; }
  body { position: relative; font-family: "Arimo", Arial, sans-serif; color: var(--ink); }

  .closing { position: absolute; left: 76px; top: 18px; font-style: italic; font-size: 22px; }
  .signature-rule { position: absolute; left: 80px; top: 183px; width: 452px; height: 2px; background: var(--rule); }

  .signer-name { position: absolute; left: 74px; top: 206px; font-family: "Cormorant SC", "Times New Roman", serif; font-weight: 500; font-size: 36px; letter-spacing: 0.5px; color: #2a2a2a; }
  .signer-role { position: absolute; left: 75px; top: 252px; font-size: 22px; color: #222; }

  .brand-mark { position: absolute; left: 76px; top: 318px; width: 200px; height: 160px; }
  .brand-mark .brand-square { position: absolute; left: 10px; top: 8px; width: 96px; height: 96px; background: var(--gold); }
  .brand-mark .brand-name { position: absolute; left: 0; top: 124px; font-size: 15px; font-weight: 700; color: var(--gold); letter-spacing: 0.3px; white-space: nowrap; }

  .company { position: absolute; left: 290px; top: 294px; font-size: 22.5px; line-height: 30px; color: #222; }
  .company-name { font-weight: 700; font-size: 23.5px; color: var(--grey-text); }
  .company-name .accent { color: var(--gold); }
  .company .label { font-weight: 700; }
  .company .sep { padding: 0 8px; }
  .company .email { color: var(--link-muted); text-decoration: underline; }
  .company .web { color: var(--gold); }

  .social { position: absolute; left: 948px; top: 435px; display: flex; gap: 27px; }
  .social span { width: 50px; height: 50px; border-radius: 8px; display: block; }
  .social .one { background: var(--icon-blue); }
  .social .two { background: var(--icon-sky); }
  .social .three { background: var(--icon-navy); }

  .banner { position: absolute; left: 0; top: 496px; width: 1200px; height: 282px;
    background: linear-gradient(180deg, var(--band-top) 0%, var(--band-mid) 45%, var(--band-green) 78%, #9fdc5e 100%); }

  .legal { position: absolute; left: 0; top: 778px; width: 1200px; height: 244px;
    background: linear-gradient(180deg, var(--foot-top) 0%, var(--foot-bottom) 100%); }
  .legal p { position: absolute; left: 63px; width: 1110px; font-size: 21px; line-height: 29px; color: #222; }
  .legal .notice { top: 12px; }
  .legal .error-note { top: 120px; }
  .legal .error-note a { color: var(--link); }
  .eco-mark { position: absolute; left: 63px; top: 187px; width: 52px; height: 52px; background: var(--eco-green); }
  .legal .print-note { top: 220px; left: 143px; font-style: italic; font-size: 16px; line-height: 20px; color: #333; }
</style>
</head>
<body>
  <p class="closing">Yours sincerely,</p>
  <div class="signature-rule"></div>

  <h1 class="signer-name">Benedict Harlowe</h1>
  <p class="signer-role">Licensed Strata and Community Manager</p>

  <div class="brand-mark">
    <span class="brand-square"></span>
    <span class="brand-name">CARRODY ESTATE</span>
  </div>

  <div class="company">
    <div class="company-name"><span class="accent">CARRODY</span> ESTATE HOLDINGS PTY LTD</div>
    <div>143 Tallowood Street,</div>
    <div>KELDARRA NSW 2093</div>
    <div><span class="label">P</span>: 02.9473.6820<span class="sep">|</span><span class="label">F</span>: 9536.2048</div>
    <div><span class="label">E</span>: <span class="email">info@carrodyestate.com.au</span></div>
    <div>Website: <span class="web">www.carrodyestate.com.au</span></div>
  </div>

  <div class="social" aria-label="Social links">
    <span class="one"></span><span class="two"></span><span class="three"></span>
  </div>

  <div class="banner" role="img" aria-label="Photo of miniature business figures walking along green paper cut-out townhouse fronts"></div>

  <div class="legal">
    <p class="notice">This e-mail message and accompanying data may contain information that is confidential and private. If you are not the intended recipient, the use, dissemination, distribution or copying of this message or data is prohibited.</p>
    <p class="error-note">If you have received this e-mail in error please notify us immediately and delete all material pertaining to this e-mail. <a href="mailto:strata@carrodyestate.com.au">strata@carrodyestate.com.au</a></p>
    <span class="eco-mark" role="img" aria-label="Environment icon"></span>
    <p class="print-note">Please consider the environment - do you really need to print this email?</p>
  </div>
</body>
</html>
```